Designer Instructions – Updated Referral Program Flyer

(Based on the mock-up in “Brief Layout and Instructions.pdf”)

OVERALL STYLE + LAYOUT

Maintain the same general layout, structure, and flow as the mock-up flyer (front and back).

This is an update of an older flyer, not a full redesign — keep the same sections, proportions, and overall visual feel, but with cleaner, more modern design improvements.

The final flyer should look clean, bold, professional, and high-impact, geared toward realtors, property managers, and contractors who refer work.

FRONT SIDE INSTRUCTIONS
1. Header Section

Remove the Tallow Ridge Builders logo from the top banner.
(Shown on page 1 of the PDF)

2. Main Headline

Keep the same three-line structure:
EARN
UNLIMITED
CASH

Center it, maximize impact, and increase the font size of CASH so all three words match in importance.

Make the headline bold, clean, and the main focal point.

3. Cash Incentive Box

Keep the "$500 minimum OR 10% per referral" box, but upgrade the graphics to look sharper and more modern.

Ensure the wording matches exactly what’s in the mock-up.

4. Premier Partner Program Ribbon

Clean up and modernize the "PREMIER PARTNER PROGRAM" bar while keeping the same position and structure.

Ensure the checkmark badge remains crisp and professional.

5. Supporting Icons Section

Keep the four icons/benefit boxes (Guaranteed Payout, Free Evaluations, Affordable Solutions, Industry Leaders) in the same order.

Update the icons to cleaner, more modern styles — but maintain the same meanings.

Improve alignment and spacing for sharper visual consistency.

6. Remove Icons in Contact Area

At the bottom (“CALL TEXT OR BOOK ONLINE 555-014-2796 TallowRidgeBuilders.example”), remove the phone and internet icons, as noted on page 2 of the PDF.

7. Replace All Images

I (Darnell) will provide all updated stock images separately via email.

Replace the flood/water-damage imagery and roof leak with the new images I send.

Keep image placement and proportions the same as the mock-up.

BACK SIDE INSTRUCTIONS
1. Header Image + “REFER / EARN” Section

Maintain the same large split-image layout (“The more you refer, the more you earn”).

Replace all background imagery with the new assets I will send.

Keep the CASH FLOW image section but modernize the type and spacing.

2. “HOW IT WORKS” Section

Preserve the three-column layout:

Refer Flood, Water & Mold Damage

We Take Care of Everything (evaluations/insurance)

Get Paid to Share

Update images, tighten spacing, and use modern iconography.

3. Remove Phone/Internet Icons

Same as the front side — remove small communication icons and keep only the text/number/URL.

4. Bottom Contact Bar

Keep the blue bar, same wording, same layout — just modernize the style if needed for clarity.

5. Replace All Back-Side Images

Again, I will email you the image assets.

Keep the layout EXACT — just update with higher-quality photos and improved design.

TEXT CONTENT (Keep as-is unless spacing adjustments needed)

All text shown in the PDF should remain exactly the same unless spacing or visual balance requires minor adjustments.
Example from page 3:

“REFER FLOOD, MOLD & CONSTRUCTION JOBS”

“We Schedule a Free Estimate. If Approved, You Get Paid.”

“Everybody Benefits From Referrals”

Everything stays, just refreshed and visually improved.

DESIGN GOALS

Flyer should look high-end and trustworthy, not salesy.

Consistent color theme: blues, whites, yellows, same palette as original.

Use bold, modern fonts with strong readability.

Ensure all headlines pop and all benefit boxes are clean, well-aligned, and evenly spaced.

The final result should feel like a premium referral program flyer for a top-tier restoration/remodel company.

FILES I WILL PROVIDE

I will send the designer:

All replacement stock photos

Any updated logos (if needed)

Original high-resolution version of the mock-up (if available)

Any additional icons preferred

0054AA
0677BA
7BADD7
CADEEF
E8F1F8

• Designer Instructions – Updated Referral Program Flyer (Based on the mock-up in “Brief Layout and Instructions.pdf”) OVERALL STYLE + LAYOUT Maintain the same general layout, structure, and flow as the mock-up flyer (front and back). This is an update of an older flyer, not a full redesign — keep the same sections, proportions, and overall visual feel, but with cleaner, more modern design improvements. The final flyer should look clean, bold, professional, and high-impact, geared toward realtors, property managers, and contractors who refer work. FRONT SIDE INSTRUCTIONS 1. Header Section Remove the Tallow Ridge Builders logo from the top banner. (Shown on page 1 of the PDF) 2. Main Headline Keep the same three-line structure: EARN UNLIMITED CASH Center it, maximize impact, and increase the font size of CASH so all three words match in importance. Make the headline bold, clean, and the main focal point. 3. Cash Incentive Box Keep the "$500 minimum OR 10% per referral" box, but upgrade the graphics to look sharper and more modern. Ensure the wording matches exactly what’s in the mock-up. 4. Premier Partner Program Ribbon Clean up and modernize the "PREMIER PARTNER PROGRAM" bar while keeping the same position and structure. Ensure the checkmark badge remains crisp and professional. 5. Supporting Icons Section Keep the four icons/benefit boxes (Guaranteed Payout, Free Evaluations, Affordable Solutions, Industry Leaders) in the same order. Update the icons to cleaner, more modern styles — but maintain the same meanings. Improve alignment and spacing for sharper visual consistency. 6. Remove Icons in Contact Area At the bottom (“CALL TEXT OR BOOK ONLINE 555-014-2796 TallowRidgeBuilders.example”), remove the phone and internet icons, as noted on page 2 of the PDF. 7. Replace All Images I (Darnell) will provide all updated stock images separately via email. Replace the flood/water-damage imagery and roof leak with the new images I send. Keep image placement and proportions the same as the mock-up. BACK SIDE INSTRUCTIONS 1. Header Image + “REFER / EARN” Section Maintain the same large split-image layout (“The more you refer, the more you earn”). Replace all background imagery with the new assets I will send. Keep the CASH FLOW image section but modernize the type and spacing. 2. “HOW IT WORKS” Section Preserve the three-column layout: Refer Flood, Water & Mold Damage We Take Care of Everything (evaluations/insurance) Get Paid to Share Update images, tighten spacing, and use modern iconography. 3. Remove Phone/Internet Icons Same as the front side — remove small communication icons and keep only the text/number/URL. 4. Bottom Contact Bar Keep the blue bar, same wording, same layout — just modernize the style if needed for clarity. 5. Replace All Back-Side Images Again, I will email you the image assets. Keep the layout EXACT — just update with higher-quality photos and improved design. TEXT CONTENT (Keep as-is unless spacing adjustments needed) All text shown in the PDF should remain exactly the same unless spacing or visual balance requires minor adjustments. Example from page 3: “REFER FLOOD, MOLD & CONSTRUCTION JOBS” “We Schedule a Free Estimate. If Approved, You Get Paid.” “Everybody Benefits From Referrals” Everything stays, just refreshed and visually improved. DESIGN GOALS Flyer should look high-end and trustworthy, not salesy. Consistent color theme: blues, whites, yellows, same palette as original. Use bold, modern fonts with strong readability. Ensure all headlines pop and all benefit boxes are clean, well-aligned, and evenly spaced. The final result should feel like a premium referral program flyer for a top-tier restoration/remodel company. FILES I WILL PROVIDE I will send the designer: All replacement stock photos Any updated logos (if needed) Original high-resolution version of the mock-up (if available) Any additional icons preferred

```html
<!DOCTYPE html>
<html lang="en">
<head>
<meta charset="utf-8">
<title>Referral Partner Program Flyer</title>
<link rel="stylesheet" href="https://fonts.googleapis.com/css2?family=Inter:wght@400;600&family=Oswald:wght@500;600;700&family=Poppins:wght@500;600;700&display=swap">
<style>
  :root {
    --blue-deep: #2d5193;
    --blue: #3b67ae;
    --title-blue: #2c4f98;
    --yellow: #f8e84a;
    --gold: #e0a03c;
    --red: #a9292d;
    --ink: #121212;
    --white: #ffffff;
    --photo: #000000;
    --caption-bg: #f2f2f2;
    --ribbon-grey: #ececec;
    --page-a: #f5e5c3;
    --page-b: #fbf4c8;
  }
  * { box-sizing: border-box; margin: 0; padding: 0; }
  html, body { width: 945px; height: 1200px; overflow: hidden; }
  body {
    background: linear-gradient(35deg, var(--page-b) 0%, var(--page-a) 70%);
    position: relative;
    font-family: "Poppins", sans-serif;
  }
  .flyer {
    position: absolute;
    left: 71px;
    width: 785px;
    height: 508px;
    background: var(--white);
    overflow: hidden;
    box-shadow: 0 2px 10px rgba(120, 90, 30, 0.12);
  }
  .flyer--front { top: 54px; }
  .flyer--back { top: 621px; }
  .abs { position: absolute; }
  .header-art { position: absolute; left: 0; top: 0; overflow: visible; }

  .gold-text {
    background: linear-gradient(90deg, var(--yellow) 35%, var(--gold) 100%);
    -webkit-background-clip: text;
    background-clip: text;
    color: transparent;
  }
  .display {
    font-family: "Oswald", sans-serif;
    font-weight: 700;
    line-height: 1;
    white-space: nowrap;
  }

  /* front headline */
  .hero-front { left: 48px; width: 190px; text-align: center; }
  .hero-front.earn { top: 10px; font-size: 90px; }
  .hero-front.unlimited { top: 98px; font-size: 43px; color: var(--white); }
  .hero-front.cash { top: 135px; font-size: 89px; }

  .tagline {
    left: 503px; top: 220px;
    font-family: "Poppins", sans-serif; font-weight: 700;
    font-size: 16.5px; line-height: 20px; color: var(--ink);
  }

  /* offer ribbon */
  .offer { left: 58px; top: 273px; width: 356px; height: 43px; }
  .offer > svg { position: absolute; left: 0; top: 0; }
  .offer .amount { position: absolute; top: 1px; font-size: 36px; }
  .offer .amount--min { left: 28px; }
  .offer .amount--pct { left: 208px; }
  .offer .label {
    position: absolute; color: var(--white);
    font-weight: 700; font-size: 11px; line-height: 1;
  }
  .offer .label--min { left: 104px; top: 16px; }
  .offer .label--per { left: 278px; top: 6px; }
  .offer .label--ref { left: 278px; top: 23px; }
  .offer .or {
    position: absolute; left: 167px; top: 9px; width: 26px; text-align: center;
    font-weight: 700; font-size: 12px; line-height: 26px; color: var(--ink);
  }

  /* partner ribbon */
  .partner { left: 449px; top: 273px; width: 281px; height: 44px; }
  .partner > svg { position: absolute; left: 0; top: 0; }
  .partner .premier {
    position: absolute; left: 0; width: 281px; top: 3px; text-align: center;
    font-weight: 500; font-size: 9.5px; letter-spacing: 5px; line-height: 12px; color: var(--ink);
  }
  .partner .program {
    position: absolute; left: 0; width: 281px; top: 19px;
    display: flex; justify-content: center; align-items: center; gap: 8px;
    font-weight: 600; font-size: 16.5px; letter-spacing: 2.6px; line-height: 24px; color: var(--white);
  }
  .partner .program svg { flex: none; }

  .section-title {
    left: 0; width: 785px; top: 334px; text-align: center;
    font-size: 27px; color: var(--ink);
  }

  /* benefits */
  .benefit { top: 382px; width: 175px; height: 46px; }
  .benefit:nth-child(1) { left: 24px; }
  .benefit:nth-child(2) { left: 212px; }
  .benefit:nth-child(3) { left: 400px; }
  .benefit:nth-child(4) { left: 587px; }
  .benefit > svg { position: absolute; left: 0; top: 0; }
  .benefit h3 {
    position: absolute; left: 48px; top: 0;
    font-family: "Oswald", sans-serif; font-weight: 600; font-size: 12px; line-height: 14px;
    color: var(--title-blue); white-space: nowrap;
  }
  .benefit p {
    position: absolute; left: 48px; top: 18px;
    font-weight: 500; font-size: 8.3px; line-height: 12.4px; color: var(--ink); white-space: nowrap;
  }

  /* footer */
  .contact-bar {
    left: 0; width: 785px;
    background: linear-gradient(90deg, var(--yellow) 0%, var(--yellow) 45%, var(--gold) 62%, var(--gold) 100%);
  }
  .flyer--front .contact-bar { top: 466px; height: 42px; }
  .flyer--back .contact-bar { top: 474px; height: 34px; }
  .contact {
    position: absolute; left: 0; width: 785px; text-align: center; white-space: nowrap;
    font-weight: 700; font-size: 12.8px; line-height: 16px; color: var(--ink);
  }
  .contact .gap { display: inline-block; width: 20px; }
  .flyer--front .contact { top: 484px; }
  .flyer--back .contact { top: 485px; }

  .slogan {
    left: 77px; top: 444px; width: 630px; height: 34px;
    background: var(--red); color: var(--white);
    font-weight: 700; font-size: 16.5px; letter-spacing: 4.3px; line-height: 34px;
    text-align: center; white-space: nowrap; padding-left: 4px;
  }

  /* back headline */
  .hero-back { left: 0; width: 340px; text-align: center; }
  .hero-back.line-white { color: var(--white); font-size: 33px; }
  .hero-back.l1 { top: 21px; }
  .hero-back.refer { top: 49px; font-size: 75px; }
  .hero-back.l3 { top: 125px; }
  .hero-back.earn { top: 154px; font-size: 74px; letter-spacing: 9px; padding-left: 9px; }

  .how-title { left: 574px; top: 235px; font-size: 27px; color: var(--ink); }

  .step {
    top: 279px; width: 211px; height: 179px;
    background: var(--caption-bg); border-radius: 3px; overflow: hidden;
  }
  .step--1 { left: 68px; }
  .step--2 { left: 292px; }
  .step--3 { left: 516px; }
  .step .photo { width: 211px; height: 125px; background: var(--photo); }
  .step h4 {
    margin-top: 12px; text-align: center;
    font-family: "Inter", sans-serif; font-weight: 600; font-size: 7.4px; line-height: 10px; color: var(--ink);
  }
  .step p {
    margin-top: 6px; text-align: center;
    font-family: "Inter", sans-serif; font-weight: 400; font-size: 8px; line-height: 11px; color: var(--ink);
  }
</style>
</head>
<body>

<section class="flyer flyer--front">
  <svg class="header-art" width="785" height="260" viewBox="0 0 785 260">
    <defs>
      <linearGradient id="goldRibbon" x1="0" x2="1" y1="0" y2="0">
        <stop offset="0.45" stop-color="#f8e84a"/>
        <stop offset="1" stop-color="#e0a03c"/>
      </linearGradient>
    </defs>
    <rect width="785" height="260" fill="var(--blue-deep)"/>
    <polygon points="236,0 785,0 785,260 411,260" fill="var(--blue)"/>
    <polygon points="437,21 785,21 785,234 444,234 339,98" fill="var(--photo)" role="img" aria-label="Photo of a flooded home interior with water damage"/>
    <polygon points="476,216 785,216 785,243 494,243" fill="url(#goldRibbon)"/>
  </svg>

  <div class="abs display gold-text hero-front earn">EARN</div>
  <div class="abs display hero-front unlimited">UNLIMITED</div>
  <div class="abs display gold-text hero-front cash">CASH</div>
  <div class="abs tagline">GET PAID TO REFER A FLOOD</div>

  <div class="abs offer">
    <svg width="356" height="43" viewBox="0 0 356 43">
      <polygon points="0,0 348,0 356,43 0,43 8,21.5" fill="var(--red)"/>
      <polygon points="180,2.5 198,12.5 198,32.5 180,42.5 162,32.5 162,12.5" fill="var(--white)"/>
    </svg>
    <span class="amount amount--min display gold-text">$500</span>
    <span class="label label--min">MINIMUM</span>
    <span class="or">OR</span>
    <span class="amount amount--pct display gold-text">10%</span>
    <span class="label label--per">PER</span>
    <span class="label label--ref">REFFERAL</span>
  </div>

  <div class="abs partner">
    <svg width="281" height="44" viewBox="0 0 281 44">
      <polygon points="13,0 268,0 272,18 9,18" fill="var(--ribbon-grey)"/>
      <polygon points="0,18 281,18 276,30.5 281,43 0,43 4,30.5" fill="var(--red)"/>
    </svg>
    <div class="premier">PREMIER</div>
    <div class="program">
      <span>PARTNER</span>
      <svg width="13" height="14" viewBox="0 0 13 14" aria-hidden="true">
        <path d="M6.5 0.5 L12.5 2.5 V7 C12.5 10.2 9.8 12.5 6.5 13.5 C3.2 12.5 0.5 10.2 0.5 7 V2.5 Z" fill="#f1c23e"/>
        <path d="M3.8 7 L5.8 9 L9.4 5.2" fill="none" stroke="var(--red)" stroke-width="1.5" stroke-linecap="round" stroke-linejoin="round"/>
      </svg>
      <span>PROGRAM</span>
    </div>
  </div>

  <h2 class="abs display section-title">PARTNER WITH US &amp; EVERYBODY WINS</h2>

  <div class="benefits">
    <div class="abs benefit">
      <svg width="40" height="44" viewBox="0 0 40 44" aria-hidden="true">
        <defs><linearGradient id="hexA" x1="0" y1="0" x2="1" y2="1"><stop offset="0" stop-color="#3a6cc0"/><stop offset="1" stop-color="#27498f"/></linearGradient></defs>
        <polygon points="19.7,0 38.7,10 38.7,33 19.7,43 0.7,33 0.7,10" fill="url(#hexA)"/>
        <circle cx="19.7" cy="21.5" r="9" fill="none" stroke="#fff" stroke-width="1.2"/>
        <circle cx="19.7" cy="21.5" r="5.5" fill="none" stroke="#fff" stroke-width="1.1"/>
        <path d="M17.2 21.6 L19 23.4 L22.4 19.8" fill="none" stroke="#fff" stroke-width="1.2" stroke-linecap="round" stroke-linejoin="round"/>
      </svg>
      <h3>GUARANTEED PAYOUT</h3>
      <p>Minimum $500 or 10% of<br>Total Invoice Paid Fast</p>
    </div>
    <div class="abs benefit">
      <svg width="40" height="44" viewBox="0 0 40 44" aria-hidden="true">
        <polygon points="19.7,0 38.7,10 38.7,33 19.7,43 0.7,33 0.7,10" fill="url(#hexA)"/>
        <rect x="12" y="12" width="13" height="18" rx="1.5" fill="none" stroke="#fff" stroke-width="1.1"/>
        <rect x="15.5" y="10.5" width="6" height="3" rx="1" fill="#fff"/>
        <circle cx="18.5" cy="18" r="3" fill="none" stroke="#fff" stroke-width="1"/>
        <path d="M14.5 24 H22.5 M14.5 27 H20" stroke="#fff" stroke-width="1"/>
        <rect x="22" y="21" width="7" height="10" rx="1" fill="url(#hexA)" stroke="#fff" stroke-width="1"/>
        <path d="M23.5 24 H27.5 M23.5 26.5 H27.5 M23.5 29 H27.5" stroke="#fff" stroke-width="0.8"/>
      </svg>
      <h3>FREE ESTIMATES</h3>
      <p>Fast &amp; Free Inspections &amp;<br>Written Estimates</p>
    </div>
    <div class="abs benefit">
      <svg width="40" height="44" viewBox="0 0 40 44" aria-hidden="true">
        <polygon points="19.7,0 38.7,10 38.7,33 19.7,43 0.7,33 0.7,10" fill="url(#hexA)"/>
        <circle cx="23" cy="16" r="4.5" fill="none" stroke="#fff" stroke-width="1.1"/>
        <path d="M23 13.8 V18.2" stroke="#fff" stroke-width="1"/>
        <path d="M10 24 H13 V31 H10 Z" fill="none" stroke="#fff" stroke-width="1.1"/>
        <path d="M13 25 L17 23.5 L22 24.5 C23.5 24.8 23.5 26.5 22 26.5 H18.5 L24 27 L28 24.5 C29.3 23.8 30.3 25.2 29.2 26.2 L24.5 30 H13" fill="none" stroke="#fff" stroke-width="1.1" stroke-linejoin="round"/>
      </svg>
      <h3>AFFORDABLE SOLUTIONS</h3>
      <p>Lowest Out of Pocket<br>Costs for Your Customers</p>
    </div>
    <div class="abs benefit">
      <svg width="40" height="44" viewBox="0 0 40 44" aria-hidden="true">
        <polygon points="19.7,0 38.7,10 38.7,33 19.7,43 0.7,33 0.7,10" fill="url(#hexA)"/>
        <circle cx="19.7" cy="13.5" r="3.5" fill="none" stroke="#fff" stroke-width="1.1"/>
        <path d="M19.7 17 V21 M12 21 H27.4 M12 21 V24 M19.7 21 V24 M27.4 21 V24" stroke="#fff" stroke-width="1"/>
        <circle cx="12" cy="27" r="2.8" fill="none" stroke="#fff" stroke-width="1.1"/>
        <circle cx="19.7" cy="27" r="2.8" fill="none" stroke="#fff" stroke-width="1.1"/>
        <circle cx="27.4" cy="27" r="2.8" fill="none" stroke="#fff" stroke-width="1.1"/>
      </svg>
      <h3>INDUSTRY LEADERS</h3>
      <p>Licensed &amp; Certified Experts<br>Provide 100% Guarantee</p>
    </div>
  </div>

  <div class="abs contact-bar"></div>
  <div class="abs slogan">SEND REFERRALS. GET PAID. GROW YOUR BUSINESS.</div>
  <p class="contact">CALL TEXT OR BOOK ON-LINE<span class="gap"></span>555-014-2796 | TallowRidgeBuilders.example</p>
</section>

<section class="flyer flyer--back">
  <svg class="header-art" width="785" height="270" viewBox="0 0 785 270">
    <defs>
      <linearGradient id="goldRibbonBack" x1="0" x2="1" y1="0" y2="0">
        <stop offset="0.35" stop-color="#f8e84a"/>
        <stop offset="1" stop-color="#e0a03c"/>
      </linearGradient>
    </defs>
    <rect width="785" height="254" fill="var(--blue-deep)"/>
    <polygon points="261,0 349,0 499,254 398,254" fill="var(--blue)"/>
    <polygon points="349,0 785,0 785,254 499,254" fill="var(--photo)" role="img" aria-label="Photo of a contractor shaking hands with a homeowner"/>
    <polygon points="550,229 785,229 785,269 568,269" fill="url(#goldRibbonBack)"/>
  </svg>

  <div class="abs display hero-back line-white l1">THE MORE YOU</div>
  <div class="abs display gold-text hero-back refer">REFER</div>
  <div class="abs display hero-back line-white l3">THE MORE YOU</div>
  <div class="abs display gold-text hero-back earn">EARN</div>

  <h2 class="abs display how-title">HOW IT WORKS</h2>

  <article class="abs step step--1">
    <div class="photo" role="img" aria-label="Photo of water damage in a home"></div>
    <h4>REFER FLOOD, MOLD &amp; CONSTRUCTION JOBS:</h4>
    <p>It’s Simple to Refer 24/7:<br>Call, Text or Book Online.</p>
  </article>
  <article class="abs step step--2">
    <div class="photo" role="img" aria-label="Photo of a technician inspecting a damaged room"></div>
    <h4>WE TAKE CARE OF EVERYTHING</h4>
    <p>We Schedule a Free Estimate.<br>If Approved, You Get Paid.</p>
  </article>
  <article class="abs step step--3">
    <div class="photo" role="img" aria-label="Photo of a freshly remodeled interior"></div>
    <h4>EVERYBODY BENEFITS FROM REFERRALS</h4>
    <p>We Provide Expert Quality<br>Work for Affordable Price.</p>
  </article>

  <div class="abs contact-bar"></div>
  <p class="contact">CALL TEXT OR BOOK ON-LINE<span class="gap"></span>555-014-2796 | TallowRidgeBuilders.example</p>
</section>

</body>
</html>
```